Website design for learning and development business

I need a logo for my new business based in Australasia. I am a kiwi who is a creative change maker working in the Learning & development space. I design experiential learning opportunities for businesses to grow and nurture their tribes. I take a holistic look at an organisation and analyse what is needed to build a positive culture with a growth mindset woven into their DNA. I would like to see designs that are based on the following word snaps - creative, interesting, tribal, journey, adaptability, engaging, fluid, architectural, bespoke, courageous, challenging .I have the logo (attached) and I Need a startup business website designed. I am a Learning and development professional who is looking at going out on my own and establishing my own business. I would like a website designed that people would go to to check out what I do, how I do, what skills I have and how to contact me. Also room for a blog/articles.

Target Market(s)

Small to medium business

Industry/Entity Type

Self employed training and consultancy company

Number of Pages Required

5+ page

Requirements
Must have
• home page, about page, contact us page, blog page, search for us page
Nice to have
• Testimonials,

```html
<!DOCTYPE html>
<html lang="en">
<head>
<meta charset="utf-8">
<title>Learning &amp; Development – Home</title>
<link rel="stylesheet" href="https://fonts.googleapis.com/css2?family=Poppins:wght@500;600;700&family=Open+Sans:ital,wght@0,400;0,600;1,400&display=swap">
<style>
:root{
  --pink:#e3117c;
  --purple:#5c1b7e;
  --grad:linear-gradient(90deg,var(--pink),var(--purple));
  --ink:#1d1d22;
  --text:#6d6d74;
  --grey-band:#9b9b9d;
  --footer-bg:#eef0f7;
  --white:#fff;
}
*{box-sizing:border-box;margin:0;padding:0}
html,body{width:1200px;height:4292px;overflow:hidden}
body{position:relative;background:var(--white);font-family:"Open Sans",sans-serif;color:var(--text)}
.abs{position:absolute}
h1,h2,h3,h4{font-family:"Poppins",sans-serif;color:var(--ink)}
.center{text-align:center}

/* hero */
.hero{left:0;top:0;width:1200px;height:650px;background:linear-gradient(160deg,#3c4a66 0%,#2a3550 40%,#50607d 70%,#303b55 100%)}
.logo-box{left:233px;top:0;width:102px;height:90px;background:rgba(120,135,165,.55);color:#fff;font:600 19px "Poppins",sans-serif;display:flex;align-items:center;justify-content:center}
.nav a{position:absolute;color:#fff;text-decoration:none;font:500 12.5px "Poppins",sans-serif;white-space:nowrap}
.btn{background:var(--grad);color:#fff;font:600 12px "Poppins",sans-serif;display:flex;align-items:center;justify-content:center;border-radius:3px;white-space:nowrap}
.hero-title{left:233px;top:276px;width:600px;color:#fff;font:500 36px/44px "Poppins",sans-serif}
.hero-text{left:231px;top:390px;width:340px;color:#e8ecf4;font-size:12.5px;line-height:19px}

/* features */
.feature{width:230px;text-align:center}
.feature svg{display:block;margin:0 auto}
.feature h3{font-size:19px;font-weight:600;margin-top:22px}
.feature p{font-size:10.5px;line-height:17px;margin-top:8px}

.section-title{font-size:36px;line-height:45px;font-weight:700}
.rule{height:2px;background:var(--grad)}
.lead{font-size:11.5px;line-height:16px}

.item h4{font-size:19px;font-weight:500}
.item p{font-size:11.5px;line-height:17px;margin-top:10px;width:280px}
.icon-dot{width:56px;height:56px;border-radius:50%;background:var(--grad);display:flex;align-items:center;justify-content:center}
.num{width:60px;height:60px;border-radius:50%;background:#fff;box-shadow:0 2px 10px rgba(0,0,0,.08);color:var(--purple);font:400 27px "Poppins",sans-serif;display:flex;align-items:center;justify-content:center}

.photo{background:linear-gradient(135deg,#d7c3b0,#7f97b5 55%,#3d5a86)}
.frame{border:7px solid;border-image:linear-gradient(180deg,var(--purple),var(--pink)) 1}

.band{left:0;top:2327px;width:1200px;height:330px;background:var(--grey-band)}
.band-title{color:#fff;font-size:36px;line-height:45px;font-weight:700}

.quote-text{font-style:italic;font-size:15px;line-height:25px;color:#55555c}

.card{width:230px;height:333px;background:#fff;box-shadow:0 3px 14px rgba(0,0,0,.07)}
.card .img{height:162px;background:linear-gradient(160deg,#dfe8f3,#5b86bd 50%,#1e3f77)}
.card h4{font-size:13px;line-height:18px;font-weight:600;text-align:center;margin:22px 22px 0}
.card p{font-size:8.5px;line-height:16px;text-align:center;margin:10px 22px 0}
.card .meta{display:flex;align-items:center;justify-content:center;gap:8px;margin-top:22px;font-size:9.5px;color:#555}
.avatar{width:22px;height:22px;border-radius:50%;background:#9a9a9e}

.footer{left:0;top:3930px;width:1200px;height:317px;background:var(--footer-bg)}
.footer h4{font-size:13.5px;font-weight:600}
.footer p{font-size:10px;line-height:18px}
.links li{list-style:none;font-size:9.5px;height:23px;color:#555}
.links li::before{content:"›";color:var(--pink);font-weight:700;margin-right:8px}
.social{width:21px;height:21px;border-radius:50%;border:1px solid var(--pink)}
.social.filled{background:var(--purple);border-color:var(--purple)}
.copy{left:0;top:4247px;width:1200px;height:45px;background:var(--grad);color:#fff;font-size:9.5px;display:flex;align-items:center;justify-content:center}
</style>
</head>
<body>

<!-- hero -->
<div class="abs hero" role="img" aria-label="Business handshake in front of a city skyline"></div>
<div class="abs logo-box">Logo</div>
<nav class="abs nav" style="left:0;top:0">
  <a style="left:554px;top:35px">Home</a>
  <a style="left:621px;top:35px">About</a>
  <a style="left:690px;top:35px">Blog</a>
  <a style="left:748px;top:35px">Contact</a>
</nav>
<div class="abs btn" style="left:855px;top:27px;width:110px;height:36px">Get a quote</div>
<h1 class="abs hero-title">Lorem ipsum dolor sit<br>amet, consectetur adipiscing.</h1>
<p class="abs hero-text">Pellentesque ipsum, aliquam ad, accumsan pellentesque quis nulla mi suscipit, eget vitae tortor odio id adipiscing nec. Nulla sed tempor.</p>

<!-- features -->
<div class="abs feature" style="left:235px;top:743px">
  <svg width="46" height="62" viewBox="0 0 46 62" fill="none" stroke="#b0157f" stroke-width="2"><path d="M11 26V15a12 12 0 0 1 24 0v11"/><rect x="4" y="26" width="38" height="33" rx="2"/></svg>
  <h3>Lorem ipsum</h3>
  <p>Lorem ipsum dolor sit amet, morbi quam pos simus vitae, gravida nisl quo neque quisque mauris hac nec variusn</p>
</div>
<div class="abs feature" style="left:485px;top:743px">
  <svg width="54" height="62" viewBox="0 0 54 62" fill="none" stroke="#8a1a80" stroke-width="2"><rect x="6" y="2" width="36" height="56" rx="2"/><path d="M12 12h24M12 20h24M12 28h16M12 36h12"/><circle cx="40" cy="46" r="11" fill="#fff"/><path d="M43 41h-5a2.5 2.5 0 0 0 0 5h4a2.5 2.5 0 0 1 0 5h-5M40 38v16"/></svg>
  <h3>Lorem ipsum</h3>
  <p>Lorem ipsum dolor sit amet, morbi quam pos simus vitae, gravida nisl quo neque quisque mauris hac nec variusn</p>
</div>
<div class="abs feature" style="left:735px;top:743px">
  <svg width="76" height="62" viewBox="0 0 76 62" fill="none" stroke="#a0167f" stroke-width="2"><circle cx="10" cy="14" r="5"/><path d="M5 24h10v18H5zM7 42v16M13 42v16M15 30l12-6"/><rect x="26" y="4" width="46" height="34"/><path d="M34 32V22M42 32V16M50 32V20M58 32V12M30 46h38M49 38v20"/></svg>
  <h3>Lorem ipsum</h3>
  <p>Lorem ipsum dolor sit amet, morbi quam pos simus vitae, gravida nisl quo neque quisque mauris hac nec variusn</p>
</div>

<!-- about intro -->
<h2 class="abs section-title center" style="left:300px;top:990px;width:600px">Lorem ipsum dolor sit<br>amet, consectetur</h2>
<div class="abs rule" style="left:570px;top:1096px;width:78px"></div>
<p class="abs lead center" style="left:380px;top:1120px;width:440px">Placerat metus rhoncus cras netus veniam, sed odio. Id non vestibuluvellus ve-hicula curabitur lorem pulvinar rutrum netus.sollicitudin</p>

<div class="abs icon-dot" style="left:244px;top:1190px"><svg width="28" height="28" viewBox="0 0 28 28" fill="none" stroke="#fff" stroke-width="1.5"><circle cx="14" cy="6" r="3"/><circle cx="6" cy="14" r="2.5"/><circle cx="22" cy="14" r="2.5"/><path d="M9 16h10v5H9zM3 24h22"/></svg></div>
<div class="abs item" style="left:322px;top:1187px"><h4>Lorem ipsum dolor</h4><p>Sondimentum velit purus, nec mi ante turnst eu eu, nec et quis sit proin lectus sed. Scerisque doquam solltudin tellus praesent sodales imperdiet</p></div>

<div class="abs icon-dot" style="left:244px;top:1307px"><svg width="26" height="26" viewBox="0 0 26 26" fill="none" stroke="#fff" stroke-width="1.6"><path d="M4 22l3-8L18 3l5 5-11 11z"/><path d="M4 22l5-1"/></svg></div>
<div class="abs item" style="left:322px;top:1304px"><h4>Lorem ipsum dolor sit</h4><p>Sondimentum velit purus, nec mi ante turnst eu eu, nec et quis sit proin lectus sed. Scerisque doquam solltudin tellus praesent sodales imperdiet</p></div>

<div class="abs icon-dot" style="left:244px;top:1427px"><svg width="28" height="28" viewBox="0 0 28 28" fill="none" stroke="#fff" stroke-width="1.6"><circle cx="14" cy="14" r="11"/><path d="M10.5 11a3.5 3.5 0 1 1 4.5 3.3c-.7.3-1 .8-1 1.7v1"/><circle cx="14" cy="20.5" r=".6" fill="#fff"/></svg></div>
<div class="abs item" style="left:322px;top:1422px"><h4>Lorem ipsum dolor</h4><p>Sondimentum velit purus, nec mi ante turnst eu eu, nec et quis sit proin lectus sed. Scerisque doquam solltudin tellus praesent sodales imperdiet</p></div>

<div class="abs frame" style="left:713px;top:1190px;width:314px;height:338px"></div>
<div class="abs photo" role="img" aria-label="Two colleagues working together at a computer" style="left:673px;top:1276px;width:334px;height:334px;border-radius:50%"></div>

<!-- learning journeys -->
<div class="abs photo" role="img" aria-label="Smiling woman and man shaking hands at a meeting" style="left:48px;top:1748px;width:410px;height:410px;border-radius:50%;background:linear-gradient(135deg,#f1ede8,#b8c6d4 50%,#53708f)"></div>
<h2 class="abs section-title" style="left:522px;top:1700px;width:500px">Bespoke Learning Built<br>for You.</h2>
<div class="abs rule" style="left:522px;top:1804px;width:78px"></div>
<p class="abs lead" style="left:522px;top:1829px;width:420px">Placerat metus rhoncus cras netus veniam, sed odio. Id non vestibuluvellus ve-hicula curabitur lorem pulvinar rutrum netus.sollicitudin</p>

<div class="abs num" style="left:520px;top:1915px">01</div>
<div class="abs item" style="left:602px;top:1912px"><h4>Lorem ipsum dolor</h4><p style="width:320px">Sondimentum velit purus, nec mi ante turnst eu eu, nec et quis sit proin lectus sed. Scerisque donec aliquam solltudin tellus praesent sodales imperdiet</p></div>
<div class="abs num" style="left:520px;top:2032px">02</div>
<div class="abs item" style="left:602px;top:2029px"><h4>Lorem ipsum dolor</h4><p style="width:320px">Sondimentum velit purus, nec mi ante turnst eu eu, nec et quis sit proin lectus sed. Scerisque donec aliquam solltudin tellus praesent sodales imperdiet</p></div>
<div class="abs num" style="left:520px;top:2150px">03</div>
<div class="abs item" style="left:602px;top:2147px"><h4>Lorem ipsum dolor</h4><p style="width:320px">Sondimentum velit purus, nec mi ante turnst eu eu, nec et quis sit proin lectus sed. Scerisque donec aliquam solltudin tellus praesent sodales imperdiet</p></div>

<!-- band -->
<div class="abs band"></div>
<h2 class="abs band-title center" style="left:200px;top:2414px;width:800px">We Design Engaging Learning Journeys for Growing Teams</h2>
<div class="abs btn" style="left:537px;top:2532px;width:126px;height:36px;font-size:11px">Book a Session</div>

<!-- testimonial -->
<h2 class="abs section-title" style="left:233px;top:2760px;width:520px">Check What’s Our Client<br>Say About Us</h2>
<div class="abs rule" style="left:233px;top:2874px;width:80px"></div>
<svg class="abs" style="left:885px;top:2762px" width="84" height="20" viewBox="0 0 84 20" fill="none" stroke-width="2"><path d="M36 10H2M10 3L2 10l8 7" stroke="#c9c9cf"/><path d="M48 10h34M74 3l8 7-8 7" stroke="#5c1b7e"/></svg>
<div class="abs photo" role="img" aria-label="Portrait of a smiling businessman at a desk" style="left:233px;top:2920px;width:232px;height:285px;background:linear-gradient(160deg,#e9eef2,#bac8d2 50%,#7d93a6)"></div>
<div class="abs" style="left:388px;top:3135px;width:109px;height:103px;background:linear-gradient(135deg,var(--pink),var(--purple));display:flex;align-items:center;justify-content:center">
  <svg width="62" height="50" viewBox="0 0 62 50" fill="#fff"><path d="M4 4h22v22c0 12-6 20-18 22l-2-7c6-2 9-6 9-11H4zM36 4h22v22c0 12-6 20-18 22l-2-7c6-2 9-6 9-11H36z"/></svg>
</div>
<p class="abs quote-text" style="left:532px;top:2915px;width:432px">Lorem ipsum dolor sit amet, consetetur sadipscing elitr, sediam nonumy eirmod tempor invidunt ut labore et dolormaliquyam erat, sed diam magna aliquyam erat, sediam voluptua ctremum bombe.Feugiat ligula faucibus magna integer nunc, elit porta mi massa id. Amet dolor magna orci, mauris id, massa arcmentum, sociis sit. Tempus amet praesent, sit convallis</p>
<div class="abs" role="img" aria-label="Handwritten signature" style="left:532px;top:3120px;width:150px;height:60px;background:linear-gradient(90deg,#ececf0,#f7f7f9)"></div>
<h4 class="abs" style="left:532px;top:3200px;font-size:17px;font-weight:600">Mira Castell</h4>
<p class="abs" style="left:532px;top:3226px;font-size:10.5px;color:#555">People &amp; Culture Lead</p>

<!-- blog -->
<h2 class="abs section-title center" style="left:300px;top:3333px;width:600px">View Our &nbsp;Latest Blog</h2>
<div class="abs rule" style="left:560px;top:3399px;width:78px"></div>
<p class="abs lead center" style="left:380px;top:3425px;width:440px">Placerat metus rhoncus cras netus veniam, sed odio. Id non vestibuluvellus ve-hicula curabitur lorem pulvinar rutrum netus.sollicitudin</p>

<article class="abs card" style="left:235px;top:3500px">
  <div class="img" role="img" aria-label="Glass office towers seen from below"></div>
  <h4>Condimentum nullmauris sit semper nulla</h4>
  <p>Lorem ipsum dolor sit ampendisse illum elit nunc suspendisse dolosed nultempor amet ac tis esent &nbsp;justo</p>
  <div class="meta"><span class="avatar"></span><span>By - Robins</span><span>|</span><span>3 Days Ago</span></div>
</article>
<article class="abs card" style="left:485px;top:3500px">
  <div class="img" role="img" aria-label="Glasses and pen resting on printed charts" style="background:linear-gradient(160deg,#f4f6f9,#b9cde4 50%,#4f82c0)"></div>
  <h4>Fringilla ac &nbsp;sed malesuda Natoque mau</h4>
  <p>Lorem ipsum dolor sit ampendisse illum elit nunc suspendisse dolosed nultempor amet ac tis esent &nbsp;justo</p>
  <div class="meta"><span class="avatar"></span><span>By - Robins</span><span>|</span><span>3 Days Ago</span></div>
</article>
<article class="abs card" style="left:735px;top:3500px">
  <div class="img" role="img" aria-label="Skyscrapers against a blue sky"></div>
  <h4>Gravida nisl qnequ equsque mauris hferma</h4>
  <p>Lorem ipsum dolor sit ampendisse illum elit nunc suspendisse dolosed nultempor amet ac tis esent &nbsp;justo</p>
  <div class="meta"><span class="avatar"></span><span>By - Robins</span><span>|</span><span>3 Days Ago</span></div>
</article>

<!-- footer -->
<footer class="abs footer">
  <h4 class="abs" style="left:233px;top:70px">Logo</h4>
  <p class="abs" style="left:233px;top:106px;width:220px">Sodales enim commodo sed lectus amet non, sem eu est arcu, id velit ullamcorper eu eros Imagtellus elementum nisl sollicitudinae eget nascetur,tellus nulla integer nunc &nbsp;bees klasd</p>
  <div class="abs" style="left:233px;top:195px;display:flex;gap:7px">
    <span class="social"></span><span class="social filled"></span><span class="social"></span><span class="social"></span>
  </div>
  <h4 class="abs" style="left:585px;top:70px">Company</h4>
  <ul class="abs links" style="left:585px;top:104px">
    <li>Home</li><li>About</li><li>Blog</li><li>Contact</li>
  </ul>
  <h4 class="abs" style="left:762px;top:70px">Global Footprint</h4>
  <div class="abs" role="img" aria-label="Dotted world map with office locations" style="left:762px;top:103px;width:201px;height:125px;background:radial-gradient(ellipse at center,#d3d6df 0%,#e3e5ec 60%,transparent 75%)"></div>
</footer>
<div class="abs copy">Copyright name © 2021. All Rights Reserved</div>

</body>
</html>
```